Visualisation Software brochure

i need a sales brochure for a new visualisation software company called Lumora Scene Studio.
The software has been specifically designed for manufacturers, distributers and retailers in the design / décor / furnishing / building industries. It allows customers can then import unlimited numbers of digital photos of rooms from their own home or take advantage of a library of pre-made photos, and then render different products from your catalogue into that photo to see what the finished look will be.
i have attached:
1) a mock up of the home page of the website
2) example of brochure wording that i have put together (although i am a little unsure about what other words i can add - so any suggestions here would be good)
3) i have attached some examples of other brochures that i like and would like similar designs
I am after a classy brochure used by a large corporate technology company that is given to executives and gives an impression of quality, trustworthiness and innovation.
• the colour blue as per the colours on my website mock up provided in the design brief
• I like simple, smart, clean and uncluttered design
• I like simple, clean and uncluttered design
• I like pictures that fit in with my technology (whether that be home and interior design, mixing virtual world and real world, visualising an idea) rather than basic stock of corporate people
Updates
Target Market(s)
marketing professionals
Industry/Entity Type
Software
Font styles to use
Look and feel
Each slider illustrates characteristics of the customer's brand and the style your logo design should communicate.

```html
<!DOCTYPE html>
<html lang="en">
<head>
<meta charset="utf-8">
<title>Lumora Scene Studio – Brochure</title>
<link href="https://fonts.googleapis.com/css2?family=Exo+2:wght@300;400;500&family=Titillium+Web:wght@300;400&display=swap" rel="stylesheet">
<style>
  :root {
    --backdrop: #ededed;
    --paper: #ffffff;
    --mint: #5fdf9f;
    --mint-box: #6cf0a9;
    --ink: #2b2b2b;
    --ink-soft: #555555;
    --brand-blue: #3b4fe0;
  }
  * { box-sizing: border-box; margin: 0; padding: 0; }
  html, body { width: 876px; height: 1200px; overflow: hidden; background: var(--backdrop); }
  .stage {
    position: relative; width: 938px; height: 1284px;
    transform: scale(0.9339); transform-origin: 0 0;
    font-family: "Titillium Web", sans-serif; color: var(--ink);
  }
  .spread {
    position: absolute; left: 50px; width: 836px; background: var(--paper);
    box-shadow: 0 2px 8px rgba(0,0,0,0.18);
  }
  .spread--top { top: 35px; height: 592px; }
  .spread--bottom { top: 641px; height: 595px; }
  .page { position: absolute; top: 0; width: 418px; height: 100%; }
  .page--left { left: 0; }
  .page--right { left: 418px; }
  .photo { position: absolute; }
  .heading {
    position: absolute; font-family: "Exo 2", sans-serif; font-weight: 300;
    color: var(--mint); font-size: 18px; line-height: 19px;
  }
  .heading--caps { font-size: 13px; letter-spacing: 0.3px; text-transform: uppercase; }
  .body-copy { position: absolute; font-size: 6.6px; line-height: 12px; color: var(--ink); text-align: justify; }
  .body-copy p + p { margin-top: 9px; }
  .body-copy--small { font-size: 5.6px; line-height: 9.6px; }
  .lead-copy {
    position: absolute; font-family: "Exo 2", sans-serif; font-weight: 300;
    color: var(--mint); text-align: justify;
  }
  .lead-copy--intro { font-size: 10px; line-height: 15.2px; }
  .lead-copy--panel { font-size: 7.1px; line-height: 9px; }
  .lead-copy strong { font-weight: 500; }
  .page-number { position: absolute; bottom: 10px; font-size: 8px; color: var(--mint); }
  .brand-mark {
    position: absolute; top: 26px; right: 20px; display: flex; align-items: center; gap: 5px;
    font-family: "Exo 2", sans-serif; font-weight: 500; font-size: 10px; color: var(--brand-blue);
  }
  .brand-mark__dot { width: 9px; height: 9px; background: var(--brand-blue); }
  .connector { position: absolute; left: 0; top: 0; overflow: visible; }
  .overlay-panel { position: absolute; background: var(--paper); }
  .step-grid {
    position: absolute; left: 103px; top: 287px; display: grid;
    grid-template-columns: 138px 138px; grid-auto-rows: 76px; column-gap: 10px; row-gap: 9px;
  }
  .step {
    background: var(--mint-box); color: #ffffff; font-family: "Exo 2", sans-serif;
    font-size: 7px; line-height: 10.5px; text-align: center; display: flex;
    align-items: center; justify-content: center; padding: 0 14px;
  }
  .tagline {
    position: absolute; right: 29px; top: 545px; font-family: "Exo 2", sans-serif;
    font-weight: 300; font-size: 13px; color: var(--mint);
  }
</style>
</head>
<body>
<div class="stage">

  <section class="spread spread--top">
    <article class="page page--left">
      <div class="brand-mark"><span class="brand-mark__dot"></span>Lumora Scene Studio</div>
      <h2 class="heading" style="left:37px; top:80px;">Innovation<br>redefining retail</h2>
      <svg class="connector" width="418" height="592">
        <polyline points="168,117 275,117 275,425" fill="none" stroke="var(--mint)" stroke-width="0.8"/>
        <circle cx="275" cy="425" r="2" fill="var(--mint)"/>
      </svg>
      <div class="body-copy" style="left:37px; top:132px; width:186px; font-size:7px; line-height:19px;">
        <p>We have a product that is rapidly being seen as the next market leader in interactive visualisation software. Lumora Scene Studio has been developed as an all-inclusive, easy-to-use solution that has been specifically designed for retail businesses within the design, décor, flooring, furnishing, building / renovation and real estate industries.</p>
      </div>
      <p class="lead-copy lead-copy--intro" style="left:37px; top:240px; width:186px;"><strong>Lumora Scene Studio</strong> is an innovative and powerful web and/or app-based platform that delivers you the capability to positively transform the overall retail experience of your customers as well as your bottom-line as it helps your customers achieve results by being able to visualise and conceptualise in real time how wonderful their real rooms or new homes could look with your products.</p>
      <div class="photo" role="img" aria-label="Laptop, desktop monitor, tablet and phone showing the visualisation website" style="left:125px; top:420px; width:285px; height:140px; background:linear-gradient(180deg,#2e2e2e 0%,#dfe6e4 40%,#f2f4f3 100%); border-radius:3px;"></div>
      <span class="page-number" style="left:35px;">1</span>
    </article>

    <article class="page page--right">
      <div class="photo" role="img" aria-label="Modern open-plan dining room interior with pendant lights" style="left:2px; top:0; width:416px; height:240px; background:linear-gradient(135deg,#d9dde0 0%,#b8b2a8 45%,#6f5a47 80%,#4a3a2e 100%);"></div>
      <div class="overlay-panel" style="left:229px; top:150px; width:175px; height:90px;"></div>
      <h2 class="heading" style="left:237px; top:160px;">The virtualised<br>solution</h2>
      <svg class="connector" width="418" height="592">
        <polyline points="306,190 382,190 382,110" fill="none" stroke="var(--mint)" stroke-width="0.8"/>
      </svg>
      <p class="lead-copy lead-copy--panel" style="left:237px; top:204px; width:167px;">Having your own branded virtual design software embedded on your website or accessible via a Pomelo and/or Verdant app will help bridge the gap between your customers' design dreams and your products. Our software helps solve one of the biggest problems many experience whilst redecorating or designing their home, which is despite looking at numerous samples, most cannot visualise or conceptualise what the finished look will be.</p>

      <h2 class="heading" style="left:65px; top:255px;">The challenge<br>for both customers<br>and retailers</h2>
      <div class="body-copy body-copy--small" style="left:65px; top:318px; width:158px;">
        <p>Gone are the days when all you needed was a showroom, a product line, and a business card. Customers are better informed, more interactive, and more selective than ever before. With access to a range of new technologies and a wide variety of online resources, these connected consumers are increasingly demanding a dynamic, seamless, integrated, consistent, accessible and personalised experience with your brand across all online, bricks-and-mortar and mobile channels.</p>
        <p>The customer must be empowered to interact across all touchpoints and channels; they want to browse and buy on their own schedules and retailers must offer equally accurate and immediate access to products and customer service. Consumers want to be inspired and be given the tools, advice and confidence to create unique, personal spaces – meaning companies need to feed this design dream and appealing to their vision is essential. The shopping experience should be built around the new reality that most consumers make their browsing and purchasing commitments online, often before they ever see the product in person.</p>
        <p>Amid ongoing economic uncertainty, true omni-channel retailers need to continue to focus on understanding the customer psyche and leveraging innovation to drive loyalty and customer engagement and ultimately increase sales.</p>
      </div>
      <div class="body-copy body-copy--small" style="left:237px; top:304px; width:167px;">
        <p>It doesn't matter what business you're in. Your customers will be able to visualise all possible product combinations for their new home – it just depends on your range. The software can easily handle 'flat surface products' including roofing, cladding, garage doors, windows and driveways/pathways to interior products such as carpet, tiles, timber and laminate flooring, doors, art work, bench tops and splash-backs.</p>
        <p>Importantly, our technology can also handle any product in 3D – whether it be furniture, lighting, floor rugs, curtains / blinds, wardrobes, household items, kitchen cabinets and bathroom fixtures. A truly unique feature allows customers to simply delete the existing item from their photo and replace it with another product from your catalogue without removing any item physically.</p>
        <p>Today's consumer doesn't just rely on technological gimmicks such as augmented reality or one in-store visit before making important investment decisions. With so much competition in the marketplace consumers are more driven than ever to shop around with the amount and quality of value-adding service the real deal breaker rather than price.</p>
        <p>It has become more about initiating the education of your customer versus waiting for them to ask for assistance. Using our technology can increase sales conversion rates as once customers have identified what products they would like to purchase they come to you as educated buyers, already having experienced a fantastic customer interaction with your brand.</p>
      </div>
      <span class="page-number" style="left:19px;">2</span>
    </article>
  </section>

  <section class="spread spread--bottom">
    <article class="page page--left">
      <div class="photo" role="img" aria-label="Person seen from behind touching a glowing network of connections over a night city" style="left:0; top:0; width:418px; height:214px; background:linear-gradient(180deg,#1c2530 0%,#34414e 55%,#6c6452 100%);"></div>
      <svg class="connector" width="418" height="595">
        <polygon points="25,213 50,213 37,233" fill="#1f2731"/>
        <polyline points="205,251 240,251 240,387 246,387" fill="none" stroke="var(--mint)" stroke-width="0.8"/>
      </svg>
      <h3 class="heading heading--caps" style="left:70px; top:242px;">Retailer benefits</h3>
      <div class="body-copy body-copy--small" style="left:70px; top:263px; width:164px; text-align:left;">
        <p>Be the market innovator and leader by combining technology and a dynamic, seamless, integrated and consistent level of customer service across all online, bricks-and-mortar and mobile channels that delivers the big wow factor</p>
        <p>Extend your reach – don't limit your technology footprint by only using Pomelo apps – our solution leverages and optimises all mobile devices and desktops (PomeloOS, Verdant, Web). This equates to a larger watershed of customers and more sales</p>
        <p>Increase brand engagement as our bespoke and scalable visualisation application will help customers build a relationship with your company, brand, and products and then share that experience within their social circles</p>
        <p>Understand buyer behaviour by receiving real usage statistics to obtain valuable insight about your customers and conduct trend analysis to determine how your future strategies can further enhance your bottom-line<br>Increased sales to further grow your business</p>
        <p>Maximise the exposure of your products by uploading your entire product catalogue into a visualisation software that makes them look real</p>
      </div>
      <h3 class="heading heading--caps" style="left:245px; top:380px;">Consumer benefits</h3>
      <div class="body-copy body-copy--small" style="left:245px; top:400px; width:163px; text-align:left;">
        <p>Reduce your customer's purchase anxiety as they will have the knowledge that the products they are choosing from your range are the right choice</p>
        <p>Greater flexibility in the way they shop by being open 24/7 and being able to engage with your brand when they want and how they want = happier customers and hence more sales</p>
        <p>An easy-to-use interface along with guided help and tutorials for those less confident with technology</p>
        <p>Being able to make informed purchasing decisions as they can easily compare a large range of your products at the touch of a computer key</p>
        <p>Improved personalised buying experience by enabling customers to use photos of their own personal spaces and incorporate your products</p>
      </div>
      <span class="page-number" style="left:30px;">3</span>
    </article>

    <article class="page page--right">
      <div class="photo" role="img" aria-label="Person holding a payment card while shopping online on a laptop" style="left:2px; top:0; width:416px; height:214px; background:linear-gradient(120deg,#c9c6c0 0%,#e4e6e8 45%,#9fa6ad 100%);"></div>
      <h2 class="heading" style="left:103px; top:236px; letter-spacing:0.4px;">Sales process<br>6 steps to success</h2>
      <div class="step-grid">
        <div class="step">Leverage the internet and the power of word-of-mouth</div>
        <div class="step">Sales consultants qualify customer requirements</div>
        <div class="step">Increase interest / desire via the website by seeing how virtualised product placement works – so that's how my house or room will look if I buy those products</div>
        <div class="step">Trial close by sales consultant – what is required for the customer to purchase</div>
        <div class="step">Combine the virtual and real worlds during an in-store or onsite consultation – virtual walk through your products combined with physical samples</div>
        <div class="step">Full sales opportunity close and determine steps to purchase / register</div>
      </div>
      <p class="tagline">It all leads to the register</p>
      <span class="page-number" style="left:19px;">4</span>
    </article>
  </section>

</div>
</body>
</html>
```